Business Card Design Project

TRX Solutions is a Electrical and Communications Services and Maintenance contractor to the Mining Oil and Gas sectors of Australia.
Our clients will be planners, Schedulers, Tradespeople and Engineers

We are yet to determine the primary colours that we will use on the business cards but the logos attached will form foundation of the colours used for logos on Business cards, Website, Uniforms, vehicles etc.

Target Market(s)

Mining engineers and shedulers

Industry/Entity Type

Contractor

Requirements
Must have
• information to be included on the card

Name: Derek Hanley
Title: Managing Director
Company: TRX Solutions Pty Ltd
Phone: 08 9XXX XXXX
Mobile 0400 318 942
email: dhanley@trxsolutionsgroup.com.au
Website www.trxsolutionsgroup.com.au

Address: U5/14 Kettering Street Ridgevale, WA 6071
Postal Address: PO Box 7183 Ridgevale WA 6981

Nice to have
• Double sided. Maybe the logo on the back

```html
<!DOCTYPE html>
<html lang="en">
<head>
<meta charset="utf-8">
<title>TRX Solutions – Business Card</title>
<link rel="stylesheet" href="https://fonts.googleapis.com/css2?family=Arimo:wght@400;700&display=swap">
<style>
  :root {
    --page-bg: #ececec;
    --navy: #0f2447;
    --navy-light: #16305a;
    --navy-dark: #0b1c3a;
    --white: #ffffff;
    --orange: #f28a1e;
    --heading: #13294d;
  }
  * { box-sizing: border-box; margin: 0; padding: 0; }
  html, body {
    width: 1200px;
    height: 900px;
    overflow: hidden;
    background: var(--page-bg);
    font-family: "Arimo", Arial, sans-serif;
  }
  .canvas {
    position: relative;
    width: 1200px;
    height: 900px;
  }
  .card {
    position: absolute;
    width: 600px;
    height: 375px;
    border-radius: 14px;
    overflow: hidden;
    box-shadow: 0 2px 6px rgba(0, 0, 0, 0.18);
  }
  .card--front {
    left: 110px;
    top: 60px;
    background: radial-gradient(ellipse at 60% 55%, var(--navy-light) 0%, var(--navy) 55%, var(--navy-dark) 100%);
  }
  .card--back {
    left: 490px;
    top: 470px;
    background: radial-gradient(ellipse at 50% 45%, var(--navy-light) 0%, var(--navy) 55%, var(--navy-dark) 100%);
  }
  .identity {
    height: 140px;
    background: var(--white);
    padding: 52px 0 0 58px;
    color: var(--heading);
    font-weight: 700;
    line-height: 1.02;
  }
  .identity__name { font-size: 21px; }
  .identity__title,
  .identity__company { font-size: 18px; }
  .contact {
    list-style: none;
    padding: 30px 0 0 70px;
    color: var(--white);
    font-size: 15.5px;
    line-height: 1.28;
  }
  .contact__item {
    position: relative;
    padding-left: 26px;
    white-space: nowrap;
  }
  .contact__item::before {
    content: "";
    position: absolute;
    left: 0;
    top: 6px;
    border-left: 8px solid var(--orange);
    border-top: 4.5px solid transparent;
    border-bottom: 4.5px solid transparent;
  }
  .contact__item--gap { margin-top: 16px; }
  .brand {
    position: absolute;
    left: 0;
    right: 0;
    top: 50%;
    transform: translateY(-50%);
    display: flex;
    align-items: center;
    justify-content: center;
    gap: 14px;
  }
  .brand__name {
    color: var(--white);
    font-size: 40px;
    font-weight: 400;
    letter-spacing: 1px;
  }
  .brand__mark {
    width: 14px;
    height: 14px;
    background: var(--orange);
  }
</style>
</head>
<body>
<main class="canvas">
  <section class="card card--front" aria-label="Business card front">
    <header class="identity">
      <p class="identity__name">Derek Hanley</p>
      <p class="identity__title">Managing Director</p>
      <p class="identity__company">TRX Solutions Pty Ltd</p>
    </header>
    <ul class="contact">
      <li class="contact__item">Phone: 08 9XXX XXXX</li>
      <li class="contact__item">Mobile 0400 318 942</li>
      <li class="contact__item">email: dhanley@trxsolutionsgroup.com.au</li>
      <li class="contact__item">Website www.trxsolutionsgroup.com.au</li>
      <li class="contact__item contact__item--gap">Address: U5/14 Kettering Street Ridgevale, WA 6071</li>
      <li class="contact__item">Postal Address: PO Box 7183 Ridgevale WA 6981</li>
    </ul>
  </section>

  <section class="card card--back" aria-label="Business card back">
    <div class="brand">
      <span class="brand__name">TRX Solutions</span>
      <span class="brand__mark" aria-hidden="true"></span>
    </div>
  </section>
</main>
</body>
</html>
```